Need Business Cards for my Business

email address: klmvertexcalibration@mailcove.com
web address: klmvertexcalibration.com
Slogan: We offer various NRB licenses
Wallace R. Pendry
Please stick with colors of Company Logo
would like the card to be more of the color example of the logo.
If you need PDF copy of logo email me at the above account.
Creative control rests with you.

Industry/Entity Type

Business

Contact Information for Business Card

I am a minimalist, but would like something to pop and stand out amongst other cards, make it memorable.

Font styles to use
Serif
Decorative
Script

```html
<!DOCTYPE html>
<html lang="en">
<head>
<meta charset="utf-8">
<title>Vertex Calibration – Business Cards</title>
<link rel="stylesheet" href="https://fonts.googleapis.com/css2?family=Arimo:wght@400;700&display=swap">
<style>
  :root {
    --stage: #1b1b1d;
    --brand-red: #e8232b;
    --brand-blue-light: #2a88c8;
    --brand-blue-dark: #1f4a73;
    --panel-white: #f3f4f6;
    --panel-grey: #dfe2e6;
    --ink-navy: #1f3f66;
    --text-white: #ffffff;
    --text-soft: #d7e6f3;
  }
  * { margin: 0; padding: 0; box-sizing: border-box; }
  html, body {
    width: 1200px; height: 960px; overflow: hidden;
    background: var(--stage);
    font-family: "Arimo", Arial, sans-serif;
  }
  .canvas { position: relative; width: 1200px; height: 960px; }

  .card {
    position: absolute;
    width: 560px; height: 320px;
    border-radius: 4px;
    overflow: hidden;
    box-shadow: 0 18px 40px rgba(0,0,0,0.55);
  }

  /* Contact side */
  .card-back { left: 560px; top: 110px; display: flex; }
  .card-back .contact-panel {
    width: 55%;
    background: linear-gradient(160deg, var(--brand-blue-light), var(--brand-blue-dark));
    color: var(--text-white);
    padding: 46px 30px;
    position: relative;
  }
  .holder-name { font-weight: 700; font-size: 21px; letter-spacing: 0.2px; white-space: nowrap; }
  .contact-list {
    position: absolute; left: 30px; bottom: 40px;
    list-style: none; font-size: 12.5px; line-height: 1.7; color: var(--text-soft);
    white-space: nowrap;
  }
  .card-back .brand-panel {
    width: 45%;
    background: linear-gradient(150deg, var(--panel-white), var(--panel-grey));
    padding: 44px 22px 40px;
    display: flex; flex-direction: column; justify-content: space-between;
  }
  .brand-lockup { display: flex; align-items: center; gap: 8px; white-space: nowrap; }
  .brand-mark { width: 12px; height: 12px; border-radius: 50%; background: var(--ink-navy); flex: none; }
  .brand-name {
    font-weight: 700; font-size: 14px; letter-spacing: 1px;
    text-transform: uppercase; color: var(--ink-navy);
  }
  .slogan { color: var(--brand-red); font-size: 13px; white-space: nowrap; }

  /* Brand side */
  .card-front {
    left: 80px; top: 500px;
    background: var(--brand-red);
    display: flex; align-items: center; justify-content: center;
  }
  .card-front .brand-lockup { gap: 16px; }
  .card-front .brand-mark { width: 30px; height: 30px; background: var(--text-white); }
  .card-front .brand-name { color: var(--text-white); font-size: 30px; letter-spacing: 2px; }
</style>
</head>
<body>
<main class="canvas">
  <section class="card card-back" aria-label="Business card, contact side">
    <div class="contact-panel">
      <h1 class="holder-name">Wallace R. Pendry</h1>
      <ul class="contact-list">
        <li>e: klmvertexcalibration@mailcove.com</li>
        <li>w: www.klmvertexcalibration.com</li>
      </ul>
    </div>
    <div class="brand-panel">
      <div class="brand-lockup">
        <span class="brand-mark"></span>
        <span class="brand-name">Vertex Calibration</span>
      </div>
      <p class="slogan">We offer various NRB licenses</p>
    </div>
  </section>

  <section class="card card-front" aria-label="Business card, brand side">
    <div class="brand-lockup">
      <span class="brand-mark"></span>
      <span class="brand-name">Vertex Calibration</span>
    </div>
  </section>
</main>
</body>
</html>
```